Flooring & Interior Design showroom

Just bought this business- Kestrel Lane Flooring & Interiors. Love our logo (we are on Kestrel Lane )and colors
Forest green, gold and black
Love that the back lists everything we do. We no longer have plenotilex but need to add in LVP/ SPC and need to take out vantor shadehub logo at the bottom and use the quib logo instead (maybe? open to suggestions)

Not in love with our cards- I want a higher end look
I hate the gradient poop color we have now.
Would love if they were all black - maybe or ??
or had a foil or embossing?

```html
<!DOCTYPE html>
<html lang="en">
<head>
<meta charset="utf-8">
<title>Kestrel Lane Flooring &amp; Interiors — Business Card</title>
<link href="https://fonts.googleapis.com/css2?family=Almendra+SC&family=PT+Sans&display=swap" rel="stylesheet">
<style>
  :root {
    --backdrop: #a9a9a9;
    --card: #050505;
    --ink: #f2f2f2;
    --ink-soft: #d9d9d9;
  }
  * { margin: 0; padding: 0; box-sizing: border-box; }
  html, body {
    width: 1200px; height: 1000px; overflow: hidden;
    background: var(--backdrop);
  }
  .canvas { position: relative; width: 1200px; height: 1000px; }
  .card {
    position: absolute; left: 294px; width: 613px; height: 352px;
    background: var(--card); border-radius: 28px; overflow: hidden;
    color: var(--ink);
  }
  .card--front { top: 93px; }
  .card--back { top: 547px; height: 351px; }
  .display { font-family: "Almendra SC", serif; }
  .sans { font-family: "PT Sans", sans-serif; }

  .brand {
    position: absolute; text-align: center; color: var(--ink-soft);
    text-transform: uppercase; line-height: 1;
  }
  .brand--front { left: 141px; top: 146px; width: 355px; font-size: 40px; }
  .brand--back { left: 56px; top: 283px; width: 140px; font-size: 14px; }
  .brand-sub { display: block; font-size: 0.34em; margin-top: 6px; letter-spacing: 1px; }
  .brand--back .brand-sub { font-size: 6px; margin-top: 3px; letter-spacing: 0.5px; }

  .person {
    position: absolute; left: 0; right: 0; top: 240px; text-align: center;
    text-transform: uppercase;
  }
  .person-name { font-size: 28px; line-height: 1; letter-spacing: 1px; }
  .person-role { font-size: 10px; letter-spacing: 2px; margin-top: 6px; }

  .partners {
    position: absolute; left: 0; right: 0; top: 310px;
    display: flex; justify-content: center; align-items: center; gap: 12px;
  }
  .partner {
    display: flex; align-items: center; gap: 5px;
    font-size: 15px; color: var(--ink); line-height: 1;
  }
  .partner-dot {
    width: 15px; height: 15px; border-radius: 50%; background: var(--ink-soft);
  }

  .services {
    position: absolute; top: 82px; left: 54px;
    display: flex;
  }
  .service-list {
    list-style: none; font-size: 19px; line-height: 22.5px;
    text-transform: uppercase; white-space: nowrap;
  }
  .service-list:nth-child(1) { width: 181px; }
  .service-list:nth-child(2) { width: 175px; }

  .contact {
    position: absolute; left: 212px; width: 360px; top: 274px;
    text-align: center; font-size: 15px; line-height: 18px; color: var(--ink);
    font-style: normal;
  }
</style>
</head>
<body>
<div class="canvas">

  <section class="card card--front">
    <div class="brand brand--front display">
      Kestrel Lane
      <span class="brand-sub">Flooring &amp; Interiors</span>
    </div>

    <div class="person display">
      <div class="person-name">Mara Pellin</div>
      <div class="person-role">Owner/ Designer</div>
    </div>

    <div class="partners sans">
      <div class="partner"><span>Northvale Shades</span><span class="partner-dot"></span></div>
      <div class="partner"><span>quib</span><span class="partner-dot"></span></div>
    </div>
  </section>

  <section class="card card--back">
    <div class="services display">
      <ul class="service-list">
        <li>·Area Rugs</li><li>·Blinds</li><li>·Carpet</li><li>·Cork</li><li>·Hardwood</li><li>·Laminate</li>
      </ul>
      <ul class="service-list">
        <li>·Sheers</li><li>·Valances</li><li>·Vinyl</li><li>·Bed Spreads</li><li>·Draperies</li><li>·LVP/ SPC</li>
      </ul>
      <ul class="service-list">
        <li>·Fabric</li><li>·Shades</li><li>·Pillows</li><li>·Shutters</li><li>·Upholstery</li><li>·Verticals</li>
      </ul>
    </div>

    <div class="brand brand--back display">
      Kestrel Lane
      <span class="brand-sub">Flooring &amp; Interiors</span>
    </div>

    <address class="contact sans">
      831-555-0148 · mara@kestrellaneflooring.com<br>
      27 Kestrel Lane, Harbor Point, CA 90000, EUA<br>
      www.kestrellaneflooring.com
    </address>
  </section>

</div>
</body>
</html>
```